London's best branded & leading residential inventory company requires sales pack design

Good Afternoon,

We are looking for design and print company to start working with. We have a couple of initial projects and will definitely have other projects in the future that we would require help with.

Below I have outlined the current projects that we need help with.

Amber Otter – www.amber-otter-demo.co.uk

SALES PACKS – We have our business development manager out in the field who is visiting current and new clients. We want to stand out and be different so are open to suggestions and ways of presenting ourselves and being front of mind. Our ideas about what we want are below, we do not want the pack to be heavy with tonnes of information.

We want to create one for the professional marketing leading brand we have. We would like the pack to be small and inter changeable.

Below are the values of the company which need to be communicated through USP’s/quotes as well as the design of the pack itself.
AO VALUES
• Professional
• Solution Driven
• Trusted Partner
• Consistent
• Progressive
• Personable
RB VALUES
• Quality
• Trusted Partner
• Solution Driven
• Progressive
• Energetic
• Personable

Below is the layout we would like to give you some clear guidance as to what to produce.

Design an A5 folder – landscape, which has the 3 cards in. Below is exactly the content required and the

Every card and side should have Amber Otter logo and strap line, Tel – 020 7946 0318 Email – bookings@amber-otter-demo.co.uk, QRSM & NEVB Accreditation

CARD 1 – Front (use branding any photos use subtly)
CUSTOMER FOCUS
- Open 7 days a week – 364 Days a year
- Inspections from 8am to 8pm
- 50 clerks during peak periods
- Dedicated bookings managers for every client

CARD 2 - Front (use branding any photos use subtly)
REPORT GUARANTEE & QUALITY
- 100% guarantee all reports back within 48 hours
- Reports created accurately and consistently using bespoke app ‘TrueLog’
- 19 point quality check from proof readers for every report
- All clerks receive monthly site inspection from Head of Training

CARD 3 – Front (use branding any photos use subtly)
WHY AMBER OTTER – Use photo Soren Pelby with below quote
“At Amber Otter we are dedicated to service, with the office support team open 7 days a week we can guarantee detailed management of the inspections 364 days a year (we do close for xmas!). Let us provide you with a great service by calling or emailing our team of dedicated Booking Managers for any needs or requirements”
The have the following bullet points below
- Over 45,000 inspections Carried out to the highest professional standards
- Trusted partner to 145 agents, including the most respected estate agents in London
- We know the value of a home, so we donate 5% of our profits in support of Harbourway - the UK's leading charity for homeless young people. (also have their logo in same colour as text - see front page of one of our reports that we have also now uploaded)

CARD 1 – BACK - TESTIMONIALS – Use the photos, logo and quotes.
Dunmores
Pemberly Stoke

CARD 2 – BACK - TESTIMONIALS – Use the photos, logo and quotes.
Tilby & Crowe
Ormand Fitch

CARD 3 – BACK - BACK - TESTIMONIALS – Use the photos, logo and quotes.
Peter R Hale
Fernleys

FRONT COVER OF FOLDER
AMBER OTTER – THE PROFESSIONAL INVENTORY COMPANY – (Use Logo & Strap line)

BACK COVER
FLYING HIGH ABOVE THE REST (The strap line)

INSIDE FRONT COVER – Use photo image of AO in the field

INSIDE BACK COVER – Use photo image of AO in the field (this section we must be able to slot the 3 cards)

CARD 4 NEW ADDITION
This needs to be a card can be perforated and divided into 4 (as per business cards), this idea being this card will be split and handed round to various people in our clients offices
So front of each card will have photo of bookings manager (use Soren Pelby for now), their name and role, must have our logo and strap line and contact details, with the words 'YOUR DEDICATED BOOKINGS MANAGER'
The BACK of each section (4 sections as to back of business card) to have our selling points, as per our reports front cover (see new upload) - must have logo and contact details as well (phone no and email)
- Open 7 days a week, 364 days a year
- Office open from 8.45am to 6.30pm
- Guaranteed 48 hour return of reports
- Over 45,000 inspections completed
- Up to 50 clerks in peak times

Target Market(s)

Estate Agents

Industry/Entity Type

It Company

Font styles to use
Other font styles liked:
• Those outlined in Brand Principles

Requirements
Nice to have
• Photos of Bookings Managers themselves - only Soren Pelby on website is current

```html
<!DOCTYPE html>
<html lang="en">
<head>
<meta charset="utf-8">
<title>Amber Otter – Customer Focus Card</title>
<link href="https://fonts.googleapis.com/css2?family=Montserrat:wght@500;800&family=Oswald:wght@400;500&family=Roboto+Condensed:wght@400;500&display=swap" rel="stylesheet">
<style>
:root{
  --navy:#1f1b50;
  --navy-deep:#1a1745;
  --teal:#0f5e43;
  --green:#17a04a;
  --green-bright:#2bb85a;
  --white:#ffffff;
  --grey-bg:#dcdcdc;
  --photo-light:#e9e9e9;
  --photo-mid:#bdbdbd;
  --orange:#e8532a;
}
*{margin:0;padding:0;box-sizing:border-box}
html,body{width:874px;height:1200px;overflow:hidden}
body{background:var(--grey-bg);position:relative;font-family:"Oswald",sans-serif}
.card{position:absolute;left:87px;width:687px;height:484px;overflow:hidden;box-shadow:0 2px 6px rgba(0,0,0,.25)}
.card-front{top:90px;background:var(--white)}
.card-back{top:619px;background:linear-gradient(135deg,var(--navy) 0%,var(--navy) 55%,#173a4c 80%,var(--teal) 100%)}
.layer{position:absolute;left:0;top:0}
.hero-photo{position:absolute;left:0;top:0;width:687px;height:264px;background:linear-gradient(100deg,var(--photo-light) 0%,#d4d4d4 45%,var(--photo-mid) 75%,#d8d8d8 100%)}
.brand{position:absolute;left:0;width:100%;text-align:center;font-family:"Oswald",sans-serif;font-weight:400}
.brand-name{line-height:1}
.brand-tagline{line-height:1}
.front-brand .brand-name{top:104px;font-size:46px;color:var(--navy)}
.front-brand .brand-tagline{top:160px;font-size:13px;color:var(--navy)}
.banner-title{position:absolute;top:245px;width:100%;text-align:center;font-family:"Montserrat",sans-serif;font-size:23px;color:var(--white);line-height:1}
.banner-title strong{font-weight:800}
.banner-title span{font-weight:500}
.headline{position:absolute;left:29px;line-height:1;font-weight:500;letter-spacing:.3px}
.headline-week{top:315px;font-size:40px;color:var(--white)}
.headline-year{top:360px;font-size:44px;color:var(--green-bright)}
.usp{position:absolute;left:382px;line-height:1;color:var(--white);font-weight:500}
.usp em{font-style:normal;color:var(--green-bright)}
.usp-hours{top:318px;font-size:20px}
.usp-clerks{top:349px;font-size:20px}
.usp-managers{top:384px;font-size:14px}
.site-url{position:absolute;top:438px;width:100%;text-align:center;font-family:"Montserrat",sans-serif;font-weight:500;font-size:13px;letter-spacing:1.4px;color:var(--white)}
.clients-title{position:absolute;top:36px;width:100%;text-align:center;font-size:19px;font-weight:500;color:var(--white);letter-spacing:.3px}
.testimonial{position:absolute;left:0;width:687px;height:100px}
.portrait{position:absolute;left:37px;top:0;width:90px;height:90px;border-radius:50%;border:3px solid var(--green);background:radial-gradient(circle at 50% 40%,#c9c9c9 0%,#8e8e8e 70%,#5c5c5c 100%)}
.quote{position:absolute;left:148px;top:17px;width:500px;font-family:"Roboto Condensed",sans-serif;font-size:9.6px;line-height:13.6px;color:var(--white)}
.attribution{position:absolute;left:148px;font-family:"Roboto Condensed",sans-serif;font-weight:500;font-size:13px;color:var(--white)}
.client-mark{position:absolute;right:34px;display:flex;align-items:center;gap:5px;font-family:"Roboto Condensed",sans-serif;font-weight:500;font-size:12px;color:var(--white)}
.client-mark i{display:block;width:11px;height:11px}
.t1{top:73px}.t2{top:183px}.t3{top:292px}
.t3 .quote,.t3 .attribution{left:151px}
.t1 .attribution,.t1 .client-mark{top:66px}
.t2 .attribution,.t2 .client-mark{top:68px}
.t3 .attribution,.t3 .client-mark{top:70px}
.back-brand .brand-name{top:405px;font-size:32px;color:var(--white)}
.back-brand .brand-tagline{top:444px;font-size:10px;color:var(--white)}
</style>
</head>
<body>

<section class="card card-front" aria-label="Card front: customer focus">
  <div class="hero-photo" role="img" aria-label="Soft greyscale photo of an inventory clerk inspecting a bedroom"></div>
  <svg class="layer" width="687" height="484" viewBox="0 0 687 484" aria-hidden="true">
    <defs>
      <linearGradient id="frontPanel" x1="0" y1="0" x2="1" y2="0.3">
        <stop offset="0" stop-color="#1f1b50"/>
        <stop offset="0.5" stop-color="#1c2f50"/>
        <stop offset="1" stop-color="#10694a"/>
      </linearGradient>
    </defs>
    <rect x="0" y="262" width="687" height="222" fill="url(#frontPanel)"/>
    <rect x="0" y="258" width="687" height="6" fill="#17a04a"/>
    <polygon points="153,225 514,225 473,298 198,298" fill="#17a04a"/>
    <rect x="0" y="428" width="687" height="34" fill="#1a1745"/>
    <rect x="0" y="426" width="687" height="2" fill="#9aa0a8"/>
    <rect x="0" y="462" width="687" height="2" fill="#9aa0a8"/>
    <rect x="0" y="464" width="687" height="20" fill="#138a46"/>
  </svg>
  <div class="front-brand">
    <div class="brand brand-name">Amber Otter</div>
    <div class="brand brand-tagline">The professional inventory company</div>
  </div>
  <div class="banner-title"><strong>CUSTOMER</strong> <span>FOCUS</span></div>
  <div class="headline headline-week">OPEN 7 DAYS A WEEK</div>
  <div class="headline headline-year">364 DAYS A YEAR</div>
  <div class="usp usp-hours">INSPECTIONS FROM <em>8AM TO 8PM</em></div>
  <div class="usp usp-clerks"><em>50 CLERKS</em> DURING PEAK PERIODS</div>
  <div class="usp usp-managers">DEDICATED BOOKINGS MANAGERS FOR EVERY CLIENT</div>
  <div class="site-url">WWW.AMBER-OTTER-DEMO.CO.UK</div>
</section>

<section class="card card-back" aria-label="Card back: client testimonials">
  <h2 class="clients-title">WHAT OUR CLIENTS SAY...</h2>

  <article class="testimonial t1">
    <div class="portrait" role="img" aria-label="Portrait photo of Tom Halsey"></div>
    <p class="quote">“ Dunmores has been working closely with Amber Otter for over six years, in which time they have carried out over 14,000 inspections for us, making them one of our largest inventory suppliers. They are a friendly and helpful team who we really feel we can trust to deliver great service time after time ”</p>
    <p class="attribution">Tom Halsey, Head of Suppliers, Dunmores</p>
    <div class="client-mark"><i style="background:var(--green)"></i>Dunmores</div>
  </article>

  <article class="testimonial t2">
    <div class="portrait" role="img" aria-label="Portrait photo of Daniel Okafor"></div>
    <p class="quote">“ Amber Otter are a professional, friendly and a great partner to work with. They are reliable, provide excellent reports and help us in ensuring our clients’s property is returned in a excellent condition- perfect for keeping our customer satisfied and giving us piece of mind ”</p>
    <p class="attribution">Daniel Okafor, Head of Property Management, Peter R Hale</p>
    <div class="client-mark"><i style="background:var(--white)"></i>PETER R HALE</div>
  </article>

  <article class="testimonial t3">
    <div class="portrait" role="img" aria-label="Portrait photo of Alex Marlowe"></div>
    <p class="quote">“ Amber Otter are a consistently outstanding Inventory company and have been for as long as we’ve used them. They get reports done quickly and accurately and their clerks are both knowledgeable and extremely helpful. They understand how estate agents work and ensure that they are making our lives as easy as possible ”</p>
    <p class="attribution">Alex Marlowe, Founder, Pemberly Stoke</p>
    <div class="client-mark"><i style="background:var(--orange)"></i>pemberly stoke</div>
  </article>

  <svg class="layer" width="687" height="485" viewBox="0 0 687 485" aria-hidden="true">
    <rect x="0" y="425" width="687" height="6" fill="#17a04a"/>
    <polygon points="174,390 514,390 473,462 198,462" fill="#17a04a"/>
  </svg>
  <div class="back-brand">
    <div class="brand brand-name">Amber Otter</div>
    <div class="brand brand-tagline">The professional inventory company</div>
  </div>
</section>

</body>
</html>
```